Resume for CEO

I need two formats of a resume created.

#1. It is 3 pages long and is the extended version.

#2. Is the 1 page resume.

Both should have the same styling. I am attaching the long and short version in word. I am also attaching a temporary picture for the resume. I will switch that out myself. Don't worry about keeping the sizing. It can be whatever you want.

There is a good website to use as a reference. http://quillpagecraft.com/
The reason I am not using this site is because they don't give you the files for editing. They make you use them to edit.

Please feel free to ask questions. I"m excited to see the ideas that come up.

End format should be in AI with PDF's. I want 1 resume that is 3-4 pages and one that is 1 page. They should have the same style.

Dale

Reason: I have only received 2 designs. Hopefully I can get more submissions.

Reason: I need to get the design finalized and I will end the project.

```html
<!DOCTYPE html>
<html lang="en">
<head>
<meta charset="utf-8">
<title>Dale R. Hartwell – Resume</title>
<link rel="stylesheet" href="https://fonts.googleapis.com/css2?family=Montserrat:wght@600;700&family=Arimo:ital,wght@0,400;0,700;1,400&display=swap">
<style>
  :root{
    --blue:#1a5a96;
    --red:#9b2322;
    --taupe:#a9a08f;
    --ink:#111111;
    --paper:#ffffff;
    --photo-warm:#b8842c;
    --photo-dark:#3a3228;
  }
  *{box-sizing:border-box;margin:0;padding:0}
  html,body{width:848px;height:1200px;overflow:hidden;background:var(--paper)}
  body{position:relative;font-family:"Arimo",Arial,sans-serif;color:var(--ink);font-size:13.6px;line-height:16px}
  .name{position:absolute;top:46px;left:0;width:848px;text-align:center;font-family:"Montserrat",sans-serif;font-weight:700;font-size:58px;line-height:66px;letter-spacing:1px}
  .name .first{color:var(--blue)}
  .name .last{color:var(--red)}
  .contact{position:absolute;top:121px;display:flex;gap:7px;font-size:13.6px;line-height:16px}
  .contact svg{flex:none;margin-top:2px}
  .contact.address{left:110px}
  .contact.phone{left:382px}
  .contact.email{left:547px}
  .title-band{position:absolute;top:179px;left:45px;width:558px;height:33px;background:var(--taupe);color:#fff;font-family:"Montserrat",sans-serif;font-weight:700;font-size:18.5px;line-height:33px;padding-left:43px;letter-spacing:.3px}
  .title-band .dot{display:inline-block;width:10px;height:10px;border-radius:50%;background:#fff;margin:0 17px 2px;vertical-align:middle}
  .title-tab{position:absolute;top:179px;left:790px;width:11px;height:33px;background:var(--taupe)}
  .portrait{position:absolute;top:167px;left:614px;width:171px;height:221px;background:linear-gradient(160deg,var(--photo-warm) 0%,#8a6226 45%,var(--photo-dark) 100%)}
  .summary{position:absolute;top:226px;left:76px;width:528px;text-align:center;font-size:13.6px;line-height:16.3px}
  .band{position:absolute;left:45px;width:756px;height:33px}
  .band svg{position:absolute;inset:0}
  .band h2{position:relative;font-family:"Montserrat",sans-serif;font-weight:700;font-size:19px;line-height:33px;color:#fff;padding-left:16px;letter-spacing:.3px}
  .band.professional{top:416px}
  .band.entrepreneurial{top:659px}
  .band.education{top:1065px}
  .role{position:absolute;left:90px;width:673px}
  .role .head{display:flex;justify-content:space-between;font-family:"Montserrat",sans-serif;font-weight:700;font-size:13px;line-height:16px;letter-spacing:.2px}
  .role .head .dates{font-family:"Arimo",Arial,sans-serif;font-weight:400;font-size:13.6px}
  .role .company{font-style:italic}
  .role p.desc{margin-top:17px}
  .education-list{position:absolute;top:1107px;left:80px;font-size:13.8px;line-height:17px}
  .education-list strong{font-weight:700}
</style>
</head>
<body>
  <h1 class="name"><span class="first">DALE</span> <span class="last">R. HARTWELL</span></h1>

  <div class="contact address">
    <svg width="20" height="18" viewBox="0 0 20 18"><path d="M10 1 L1 9 H4 V17 H8 V12 H12 V17 H16 V9 H19 Z" fill="#111"/></svg>
    <span>4810 Cedar Ridge Rd. Ste.<br>207 San Diego, CA 92130</span>
  </div>
  <div class="contact phone">
    <svg width="14" height="20" viewBox="0 0 14 20"><path d="M3 1 L6 1 L7 6 L5 7.5 C5.5 10.5 7 13 9 14.5 L11 13.3 L13 17.5 L10.5 19 C5 18 1 11 1.5 4 Z" fill="#111"/></svg>
    <span>(619) 555-0148</span>
  </div>
  <div class="contact email">
    <svg width="22" height="14" viewBox="0 0 22 14"><rect x="0.5" y="0.5" width="21" height="13" fill="#111"/><path d="M1 1 L11 8.5 L21 1" stroke="#fff" stroke-width="1.3" fill="none"/><path d="M1 13 L8 6.5 M21 13 L14 6.5" stroke="#fff" stroke-width="1"/></svg>
    <span>dalehartwell@example.com</span>
  </div>

  <div class="title-band">CHIEF EXECUTIVE OFFICER<span class="dot"></span>ENTREPRENEUR</div>
  <div class="title-tab"></div>
  <div class="portrait" role="img" aria-label="Portrait photo of the candidate"></div>

  <p class="summary">Dynamic Chief Executive Officer with over 16 years of experience in providing strategic direction and leadership for organizations in multiple markets with unique situations. &nbsp; Extensive experience transforming companies into profitable and progressive organizations using proven systematic implementation. Offers comprehensive knowledge and operational experience with highly-engineered technical manufacturing companies, ecommerce and international brand building. Effectively identifies critical business drivers in multiple markets and industries, enabling growth opportunities within a variety of departments and ultimately complete business expansion.</p>

  <section class="band professional">
    <svg width="756" height="33" viewBox="0 0 756 33"><polygon points="0,0 738,0 756,16.5 738,33 0,33" fill="var(--red)"/></svg>
    <h2>PROFESSIONAL EXPERIENCE</h2>
  </section>

  <article class="role" style="top:458px">
    <div class="head"><span>INTERIM CHIEF EXECUTIVE OFFICER</span><span class="dates">August 2013 – January 2014</span></div>
    <div class="company">Melt Street Food Co. TX, LLC: Austin, TX &nbsp;&nbsp;(www.meltstreetfood.com)</div>
    <p class="desc">Provides strategic direction as Interim CEO for this innovative gourmet food truck company aiming to be first publicly traded food truck company in the United States.</p>
  </article>

  <article class="role" style="top:555px">
    <div class="head"><span>CHIEF EXECUTIVE OFFICER</span><span class="dates">May 2009 – November 2011</span></div>
    <div class="company">Ridgeline Custom Cycles, Inc.: San Diego, CA &nbsp;&nbsp;(www.ridgelinecycles.com)</div>
    <p class="desc">Turned this ailing specialty bicycle company around through rebranding efforts and improved marketing and sales strategy, accelerating to profitable state within 12 months.</p>
  </article>

  <section class="band entrepreneurial">
    <svg width="756" height="33" viewBox="0 0 756 33"><polygon points="0,0 738,0 756,16.5 738,33 0,33" fill="var(--blue)"/></svg>
    <h2>ENTREPRENEURIAL EXPERIENCE</h2>
  </section>

  <article class="role" style="top:700px;width:640px">
    <div class="head"><span>CO- FOUNDER &amp; CHIEF EXECUTIVE OFFICER</span><span class="dates">January 2011 – Present</span></div>
    <div class="company">Northgate Media, Inc.: San Diego, CA</div>
    <p class="desc">Serves as Co-Founder and CEO for this marketing, media, branding, public relation, and corporate consulting company providing valuable resources to public, private, and non-profit sector organizations.</p>
  </article>

  <article class="role" style="top:798px;width:617px">
    <div class="head"><span>FOUNDER &amp; CHIEF EXECUTIVE OFFICER</span><span class="dates">May 2009 – Present</span></div>
    <div class="company">Apex Component Works, Inc.: San Diego, CA (www.ApexComponents.com)</div>
    <p class="desc" style="width:673px">Founded this cutting-edge company, redefining the level of technology, quality, and product weight in the bicycle component segment of the cycling industry launching toward international distribution and representation in 23 countries.</p>
  </article>

  <article class="role" style="top:911px;width:670px">
    <div class="head"><span>FOUNDER &amp; CHIEF EXECUTIVE OFFICER</span><span class="dates">December 1999 – April 2009</span></div>
    <div class="company">Trailward Outfitters, Inc.: San Diego, CA</div>
    <p class="desc" style="width:673px">Trailward Outfitters, Inc. experienced explosive revenue growth fueled by strategic purchasing partnerships, aggressive sales and marketing techniques, and new cutting-edge ecommerce technology implementation. Following the development of new verticals, watersports, and camping, Trailward Outfitters, Inc. was acquired after becoming one of nation’s largest e-commerce, mail-order, brick and mortar specialty retailers. &nbsp;Purchased by Harbor Pets Group, Inc. in 2009 by owners of &nbsp;petlane/bikelane.com.</p>
  </article>

  <section class="band education">
    <svg width="756" height="33" viewBox="0 0 756 33"><polygon points="0,0 738,0 756,16.5 738,33 0,33" fill="var(--taupe)"/></svg>
    <h2>EDUCATION</h2>
  </section>

  <ul class="education-list" style="list-style:none">
    <li><strong>General Studies &amp; Pre-Med</strong> – Coastal Hills University</li>
    <li><strong>Bachelor of Science in Business Administration/Marketing</strong> – Pacific State University</li>
  </ul>
</body>
</html>
```